Commercial, Public Works, Contractor needs a modern web design

We are a General and Engineering contracting firm with vast experience in our industry. Our focus is on Commercial, Tenant Improvement, Restaurants, and Public Works. We are opening a new business and would like that excitement and energy to show through the new web design. The colors we like are black, red and grey, we are open to color ideas. Attached is our logo design.

Industry/Entity Type

Restaurant

```html
<!DOCTYPE html>
<html lang="en">
<head>
<meta charset="utf-8">
<title>R K Halvern, Inc. — General Contractor and Engineer</title>
<link rel="stylesheet" href="https://fonts.googleapis.com/css2?family=Oswald:wght@400;500;600&family=PT+Sans:ital,wght@0,400;0,700;1,400&family=Tinos:wght@400;700&display=swap">
<style>
:root{
  --red:#c0141b;
  --red-dark:#8e0e13;
  --ink:#1c1c1c;
  --grey:#8a8a8a;
  --grey-light:#e9e9e9;
  --beige:#e6e1d8;
  --black:#0b0b0b;
  --white:#ffffff;
  --sky:#dbe7f2;
}
*{margin:0;padding:0;box-sizing:border-box}
html,body{width:689px;height:1200px;overflow:hidden;background:var(--white)}
body{position:relative;font-family:"PT Sans",Arial,sans-serif;color:var(--ink)}
.abs{position:absolute}

/* header */
.site-header{left:0;top:0;width:689px;height:80px;background:linear-gradient(90deg,#f6f8fb,#eef3f8)}
.brand{left:100px;top:22px}
.brand-row{display:flex;align-items:center;gap:6px}
.brand-mark{width:16px;height:16px;border-radius:50%;background:var(--red)}
.brand-name{font-family:"PT Sans",sans-serif;font-weight:700;font-size:17px;color:var(--red);letter-spacing:.5px}
.brand-tag{font-size:6.5px;letter-spacing:.6px;color:#333;margin-top:3px;margin-left:22px;text-transform:uppercase}
.main-nav{left:336px;top:35px;display:flex;gap:14px;font-family:"Tinos",serif;font-size:9px;letter-spacing:.3px}
.main-nav a{color:#222;text-decoration:none;text-transform:uppercase;padding-bottom:5px}
.main-nav a.active{color:var(--red);border-bottom:2px solid var(--red)}

/* hero */
.hero{left:0;top:80px;width:689px;height:242px;background:linear-gradient(115deg,#9fbad6 0%,#e4edf5 40%,#c6d7e8 70%,#f2f5f8 100%)}
.hero-bar{left:0;top:295px;width:689px;height:27px;background:rgba(20,20,20,.85)}
.hero-slogan{left:100px;top:298px;font-family:"Oswald",sans-serif;font-style:italic;font-weight:500;font-size:15px;color:var(--white);letter-spacing:.4px}
.hero-dots{left:565px;top:305px;display:flex;gap:5px}
.hero-dots span{width:6px;height:6px;border-radius:50%;background:var(--white)}
.hero-dots span.on{background:var(--red)}

/* welcome */
.welcome{left:0;top:322px;width:689px;height:108px;background:var(--grey-light)}
.welcome-title{left:0;top:332px;width:689px;text-align:center;font-family:"Oswald",sans-serif;font-weight:500;font-size:18px;letter-spacing:2px;color:#111}
.welcome-title .name{color:var(--red)}
.welcome-text{left:98px;top:360px;width:494px;text-align:center;font-size:6.3px;line-height:13px;color:#666}
.more-link{font-size:7px;color:#333;text-decoration:underline}
.welcome .more-link{position:absolute}
.welcome-rule{left:0;top:428px;width:689px;height:3px;background:var(--red);border-bottom:1px solid #333}

/* services tabs */
.services{left:0;top:431px;width:689px;height:127px;background:var(--beige)}
.service-divider{top:431px;width:1px;height:110px;background:#cfc8bd}
.service-tab{top:482px;width:150px;text-align:center;font-family:"Tinos",serif;font-size:11px;color:#9a9281;text-transform:uppercase}
.service-tab.active{color:var(--red)}
.service-knob{top:534px;width:40px;height:24px;border-radius:20px 20px 0 0;background:#bdb6a9}
.service-knob.active{background:var(--red)}

/* statement */
.statement{left:0;top:558px;width:689px;height:214px;background:linear-gradient(100deg,#a0161b 0%,#c0262a 45%,#8e1014 100%)}
.statement-head{left:102px;top:602px;width:480px;font-size:20.5px;line-height:26px;color:var(--white)}
.statement-text{left:102px;top:696px;width:490px;text-align:center;font-size:6.3px;line-height:12px;color:#f4dede}
.statement .more-link,.statement-more{color:var(--white)}
.statement-more{left:337px;top:738px}

/* projects */
.projects{left:0;top:772px;width:689px;height:236px;background:linear-gradient(180deg,#121212 0%,#1e1e1e 60%,#5a5a5a 78%,#3b3b3b 100%)}
.projects-title{left:0;top:784px;width:689px;text-align:center;font-size:19px;color:#e7e7e7}
.project-card{box-shadow:0 4px 10px rgba(0,0,0,.6)}
.arrow-btn{width:22px;height:22px;border:1.5px solid #aaa;border-radius:50%}

/* clients */
.clients{left:0;top:1008px;width:689px;height:54px;background:linear-gradient(180deg,#8b8b8b,#a5a5a5)}
.clients-label{left:103px;top:1028px;font-size:13px;color:var(--white)}
.clients-rule{left:188px;top:1022px;width:1px;height:26px;background:#d0d0d0}
.clients-list{left:214px;top:1023px;display:flex;gap:28px;align-items:center;font-family:"PT Sans",sans-serif;font-weight:700;font-size:19px;color:#dcdcdc;letter-spacing:.5px}

/* footer */
.site-footer{left:0;top:1062px;width:689px;height:138px;background:var(--black)}
.foot-head{top:1084px;font-size:9.5px;font-weight:700;color:var(--white);padding-bottom:4px;border-bottom:1px solid #333;width:100px}
.quick-links{left:101px;top:1105px;list-style:none;font-size:7px;line-height:15.5px;color:#ddd}
.quick-links li{display:flex;align-items:center;gap:6px}
.quick-links li::before{content:"";width:5px;height:5px;border-radius:50%;border:1px solid #aaa}
.quick-links li.active{color:var(--red)}
.quick-links li.active::before{border-color:var(--red)}
.news{left:222px;top:1105px;width:112px;font-size:6.8px;color:#bbb;line-height:9px}
.news .date{color:var(--red);font-weight:700}
.news p{margin-bottom:14px}
.support{left:356px;top:1105px;width:120px;font-size:6.8px;color:#bbb;line-height:9px}
.support .phone{font-family:"Oswald",sans-serif;font-size:16px;color:var(--white);margin:4px 0 2px;line-height:20px}
.support .mail{color:var(--red)}
.foot-brand{left:500px;top:1092px;width:92px;text-align:center}
.foot-brand .brand-name{font-size:12px;color:#9a9a9a}
.foot-brand .brand-mark{width:12px;height:12px;background:#9a9a9a}
.copyright{left:500px;top:1148px;width:92px;text-align:center;font-size:6px;color:#aaa}
.social{left:510px;top:1161px;display:flex;gap:4px}
.social span{width:11px;height:11px;border:1px solid #888;border-radius:50%}
.foot-rule{left:0;top:1197px;width:689px;height:3px;background:var(--red)}
</style>
</head>
<body>

<header class="site-header abs">
  <div class="brand abs">
    <div class="brand-row"><span class="brand-mark"></span><span class="brand-name">R K HALVERN, INC.</span></div>
    <div class="brand-tag">General Contractor and Engineer</div>
  </div>
  <nav class="main-nav abs">
    <a class="active" href="#">Home</a><a href="#">About Us</a><a href="#">Services</a><a href="#">Projects</a><a href="#">Contact Us</a>
  </nav>
</header>

<section class="hero abs" role="img" aria-label="Engineering blueprint with drafting tools, compass and pencil"></section>
<div class="hero-bar abs"></div>
<div class="hero-slogan abs">WE ARE THE LEADING ENGINEERING CONTRACTOR</div>
<div class="hero-dots abs"><span></span><span class="on"></span><span></span><span></span></div>

<section class="welcome abs">
</section>
<h1 class="welcome-title abs">WELCOME TO&nbsp; <span class="name">R K HALVERN, INC.</span></h1>
<p class="welcome-text abs">Sed ut perspiciatis unde omnis iste natus error sit voluptatem accusantium doloremque laudantium, totam rem aperiam, eaque ipsa quae ab illo inventore veritatis et quasi architecto beatae vitae dicta sunt explicabo. Nemo enim ipsam voluptatem quia voluptas sit aspernatur aut odit aut fugit, sed quia. Totam rem aperiam, eaque ipsa quae ab illo inventore veritatis et quasi architecto beatae vitae dicta sunt explicabo. Nemo enim ipsam voluptatem quia voluptas sit aspernatur aut odit aut fugit, sed quia consequuntur magni dolores eos qui ratione volupt.</p>
<a class="more-link abs" style="left:574px;top:414px" href="#">more</a>
<div class="welcome-rule abs"></div>

<section class="services abs"></section>
<div class="service-divider abs" style="left:202px"></div>
<div class="service-divider abs" style="left:356px"></div>
<div class="service-divider abs" style="left:475px"></div>
<div class="service-tab abs active" style="left:76px">Commercial</div>
<div class="service-tab abs" style="left:204px">Tenant Improvement</div>
<div class="service-tab abs" style="left:341px">Restaurants</div>
<div class="service-tab abs" style="left:463px">Public Works</div>
<div class="service-knob abs active" style="left:129px"></div>
<div class="service-knob abs" style="left:255px"></div>
<div class="service-knob abs" style="left:394px"></div>
<div class="service-knob abs" style="left:520px"></div>

<section class="statement abs" role="img" aria-label="Engineer in a hard hat reading plans at a construction site, red tinted"></section>
<h2 class="statement-head abs">Sed ut perspiciatis unde omnis iste natus error sit voluptatem accusantium doloremque laudantium, totam rem aperiam, eaque ipsa quae ab</h2>
<p class="statement-text abs">Sed ut perspiciatis unde omnis iste natus error sit voluptatem accusantium doloremque laudantium, totam rem aperiam, eaque ipsa quae ab illo inventore veritatis et quasi architecto beatae vitae dicta sunt explicabo. Nemo enim ipsam voluptatem quia voluptas sit aspernatur aut odit aut fugit, sed quia consequu.</p>
<a class="more-link statement-more abs" href="#">more</a>

<section class="projects abs"></section>
<h2 class="projects-title abs">Our Latest Projects</h2>
<div class="arrow-btn abs" style="left:66px;top:870px"></div>
<svg class="abs" style="left:72px;top:876px" width="10" height="10" viewBox="0 0 10 10"><path d="M6.5 1.5 3 5l3.5 3.5" fill="none" stroke="#ccc" stroke-width="1.5"/></svg>
<div class="arrow-btn abs" style="left:599px;top:870px"></div>
<svg class="abs" style="left:605px;top:876px" width="10" height="10" viewBox="0 0 10 10"><path d="M3.5 1.5 7 5 3.5 8.5" fill="none" stroke="#ccc" stroke-width="1.5"/></svg>
<div class="project-card abs" style="left:106px;top:864px;width:62px;height:84px;background:linear-gradient(160deg,#f0a040,#7a3a08)" role="img" aria-label="Project photo: industrial machinery detail"></div>
<div class="project-card abs" style="left:169px;top:847px;width:60px;height:107px;background:linear-gradient(180deg,#c9d6e2,#5b6e80)" role="img" aria-label="Project photo: aircraft over city skyline"></div>
<div class="project-card abs" style="left:521px;top:877px;width:63px;height:83px;background:linear-gradient(180deg,#8fb6dc,#b9b9b9)" role="img" aria-label="Project photo: modern public building"></div>
<div class="project-card abs" style="left:460px;top:847px;width:59px;height:107px;background:linear-gradient(180deg,#9fb5c9,#5e6c78)" role="img" aria-label="Project photo: marina with boats"></div>
<div class="project-card abs" style="left:230px;top:820px;width:229px;height:150px;background:linear-gradient(180deg,#1f3f6a 0%,#6f9fd2 45%,#cfe1f2 70%,#3a4c63 100%)" role="img" aria-label="Project photo: glass office towers seen from below"></div>

<section class="clients abs"></section>
<div class="clients-label abs">OUR CLIENTS</div>
<div class="clients-rule abs"></div>
<svg class="abs" style="left:198px;top:1030px" width="8" height="10" viewBox="0 0 8 10"><path d="M7 0 0 5l7 5z" fill="#e6e6e6"/></svg>
<div class="clients-list abs"><span>NORTHWAY</span><span>BRISKO</span><span>KALDER</span></div>
<svg class="abs" style="left:578px;top:1030px" width="8" height="10" viewBox="0 0 8 10"><path d="M1 0 8 5l-7 5z" fill="#e6e6e6"/></svg>

<footer class="site-footer abs"></footer>
<div class="foot-head abs" style="left:101px">QUICK LINKS</div>
<ul class="quick-links abs">
  <li class="active">HOME</li><li>ABOUT US</li><li>SERVICES</li><li>PROJECTS</li><li>CONTACT US</li>
</ul>
<div class="foot-head abs" style="left:222px">LATEST NEWS</div>
<div class="news abs">
  <p><span class="date">07 Feb., 2015</span><br><i>At vero eos et accusamus et iusto odio dignis- simos ducimus qui</i></p>
  <p><span class="date">05 Feb., 2015</span><br><i>At vero eos et accusamus et iusto odio dignis- simos ducimus qui</i></p>
</div>
<div class="foot-head abs" style="left:356px;width:110px">ONLINE SUPPORT</div>
<div class="support abs">
  <i>At vero eos et accusamus et iusto odio dignis- simos ducimus quos et accusamus et iusto odio.</i>
  <div class="phone">012 555 0147</div>
  <div>Ask your questions by E-mail</div>
  <div class="mail">support@rkhalvern.com</div>
</div>
<div class="foot-brand abs">
  <div class="brand-row" style="justify-content:center"><span class="brand-mark"></span><span class="brand-name">R K HALVERN, INC.</span></div>
</div>
<div class="copyright abs">© 2015. All rights Reserved.</div>
<div class="social abs"><span></span><span></span><span></span><span></span></div>
<div class="foot-rule abs"></div>

</body>
</html>
```